wine label for a new vineyard

We have developing vineyard which is just starting production. It izs called Wattle Brook Vineyard. It's in rural Australia and the vineyard is on top of a hill where a prominent tree type is pine (technically Calitris). We want a wine label that incorporates these elements (pine trees, hill or ridge). The calitris pines are statuesque in shape, with sillouetes varying from Lombardy pines to Pencil pines. People often chose wines by the label and we are aiming for the upper end of the market so want a label which encourages buyers to believe that this is a sophisticated product. We need to be able to superimpose the grape variety, year and other information so it needs to be uncluttered design.

Target Market(s)

Experienced and discriminating wine drinkers. Prepared to pay $ 20 for a wine they appreciate.

Industry/Entity Type

Product

Requirements
Must have
• Some element of pines and ridge (or hill) so that people associate the name and the label design.
A label which leads the viewer to believe that this is a high quality product.
Nice to have
• We would like to be able to use some elements from the label as a logo.
Should not have
• Jokey wine labels are fashionable but we don't think they suit our segement of the market.

```html
<!DOCTYPE html>
<html lang="en">
<head>
<meta charset="utf-8">
<title>Wattle Brook Vineyard – Wine Label</title>
<link rel="stylesheet" href="https://fonts.googleapis.com/css2?family=Dancing+Script:wght@700&display=swap">
<style>
  :root {
    --page: #ffffff;
    --silver-edge: #2a2a2a;
    --silver-mid: #8f8f8f;
    --silver-light: #c9c9c9;
    --frame: #3d5452;
    --copper: #a0604f;
    --teal: #3f7d78;
    --moon: #d9dcdc;
  }
  html, body {
    margin: 0;
    padding: 0;
    width: 1200px;
    height: 971px;
    overflow: hidden;
    background: var(--page);
  }
  .canvas {
    position: relative;
    width: 1200px;
    height: 971px;
  }
  .label {
    position: absolute;
    top: 96px;
    width: 520px;
    height: 780px;
  }
  .label--classic { left: 40px; }
  .label--bright { left: 640px; }
  .label svg {
    position: absolute;
    inset: 0;
    width: 520px;
    height: 780px;
  }
  .label-name {
    position: absolute;
    left: 0;
    top: 462px;
    width: 520px;
    text-align: center;
    font-family: "Dancing Script", cursive;
    font-weight: 700;
    font-size: 44px;
    line-height: 46px;
    color: var(--copper);
  }
  .label-name span { display: block; }
</style>
</head>
<body>
<main class="canvas">

  <section class="label label--classic">
    <svg viewBox="0 0 520 780" xmlns="http://www.w3.org/2000/svg">
      <defs>
        <linearGradient id="foil-classic" x1="0" x2="1" y1="0" y2="0">
          <stop offset="0" stop-color="var(--silver-edge)"/>
          <stop offset="0.3" stop-color="var(--silver-mid)"/>
          <stop offset="0.5" stop-color="var(--silver-light)"/>
          <stop offset="0.7" stop-color="var(--silver-mid)"/>
          <stop offset="1" stop-color="var(--silver-edge)"/>
        </linearGradient>
        <linearGradient id="scene-tones" x1="0" x2="1" y1="0" y2="1">
          <stop offset="0" stop-color="var(--moon)"/>
          <stop offset="0.45" stop-color="var(--copper)"/>
          <stop offset="1" stop-color="var(--teal)"/>
        </linearGradient>
      </defs>
      <rect class="label-foil" width="520" height="780" fill="url(#foil-classic)" role="img" aria-label="Silver foil label with fine scale pattern"/>
      <path class="label-frame" fill="none" stroke="var(--frame)" stroke-width="3"
        d="M260,78 Q245,80 240,100 Q200,115 160,110 Q120,140 100,170 Q60,175 62,230 L62,550 Q60,605 100,610 Q120,640 160,670 Q200,665 240,680 Q245,700 260,702 Q275,700 280,680 Q320,665 360,670 Q400,640 420,610 Q460,605 458,550 L458,230 Q460,175 420,170 Q400,140 360,110 Q320,115 280,100 Q275,80 260,78 Z"/>
      <rect class="label-scene" x="100" y="140" width="320" height="300" rx="10" fill="url(#scene-tones)" role="img" aria-label="Illustration of pale moon behind copper mountain ridge with three teal pine trees"/>
    </svg>
    <div class="label-name"><span>Wattle Brook</span><span>Vineyard</span></div>
  </section>

  <section class="label label--bright">
    <svg viewBox="0 0 520 780" xmlns="http://www.w3.org/2000/svg">
      <defs>
        <linearGradient id="foil-bright" x1="0" x2="1" y1="0" y2="0">
          <stop offset="0" stop-color="var(--silver-edge)"/>
          <stop offset="0.25" stop-color="var(--silver-mid)"/>
          <stop offset="0.5" stop-color="#e2e2e2"/>
          <stop offset="0.75" stop-color="var(--silver-mid)"/>
          <stop offset="1" stop-color="var(--silver-edge)"/>
        </linearGradient>
        <linearGradient id="scene-tones-bright" x1="0" x2="1" y1="0" y2="1">
          <stop offset="0" stop-color="var(--moon)"/>
          <stop offset="0.45" stop-color="var(--copper)"/>
          <stop offset="1" stop-color="var(--teal)"/>
        </linearGradient>
      </defs>
      <rect class="label-foil" width="520" height="780" fill="url(#foil-bright)" role="img" aria-label="Bright silver foil label with fine scale pattern"/>
      <path class="label-frame" fill="none" stroke="var(--frame)" stroke-width="3"
        d="M260,78 Q245,80 240,100 Q200,115 160,110 Q120,140 100,170 Q60,175 62,230 L62,550 Q60,605 100,610 Q120,640 160,670 Q200,665 240,680 Q245,700 260,702 Q275,700 280,680 Q320,665 360,670 Q400,640 420,610 Q460,605 458,550 L458,230 Q460,175 420,170 Q400,140 360,110 Q320,115 280,100 Q275,80 260,78 Z"/>
      <rect class="label-scene" x="100" y="140" width="320" height="300" rx="10" fill="url(#scene-tones-bright)" role="img" aria-label="Illustration of pale moon and small bird above copper mountain ridge with three teal pine trees"/>
    </svg>
    <div class="label-name"><span>Wattle Brook</span><span>Vineyard</span></div>
  </section>

</main>
</body>
</html>
```